Need updated stationery design for chiropractic clinic

We recently moved our office and are looking to refresh our letterhead, business cards, presentation folder and envelopes. I tend to prefer simple, clean designs. We communicate with a lot of attorneys and want to exude professionalism. I have attached our logo and 2 additional versions (all white and white letters instead of grey).

Target Market(s)

Other medical professionals and attorneys. Business cards will go to patients as well.

Industry/Entity Type

Healthcare

```html
<!DOCTYPE html>
<html lang="en">
<head>
<meta charset="utf-8">
<title>Northvale Clinic Letterhead</title>
<link href="https://fonts.googleapis.com/css2?family=Lato:wght@400;700&family=Montserrat:wght@400;500;700&family=Dancing+Script:wght@500&display=swap" rel="stylesheet">
<style>
  :root {
    --backdrop: #e6e6e6;
    --paper: #ffffff;
    --ink: #2f2f2f;
    --ink-soft: #555555;
    --brand-blue: #0a94c8;
    --brand-teal: #3fb3c3;
  }
  * { box-sizing: border-box; margin: 0; padding: 0; }
  html, body { width: 1200px; height: 874px; overflow: hidden; }
  body {
    background: var(--backdrop);
    font-family: "Lato", sans-serif;
    color: var(--ink);
    position: relative;
  }
  .letterhead {
    position: absolute;
    left: 300px; top: 13px;
    width: 600px; height: 848px;
    background: var(--paper);
    box-shadow: 0 2px 10px rgba(0,0,0,.12);
    overflow: hidden;
  }
  .brand {
    position: absolute; left: 52px; top: 70px;
    display: flex; align-items: center; gap: 10px;
  }
  .brand-square { width: 22px; height: 22px; background: var(--brand-blue); }
  .brand-name {
    font-family: "Montserrat", sans-serif;
    font-weight: 700; font-size: 26px;
    color: var(--brand-blue); letter-spacing: .3px;
  }
  .contact {
    position: absolute; right: 52px; top: 58px;
    border-left: 1px solid var(--brand-blue);
    padding-left: 10px;
    font-family: "Montserrat", sans-serif;
    font-size: 8px; line-height: 1.6; color: var(--ink-soft);
  }
  .contact-line { display: flex; align-items: center; gap: 5px; }
  .contact-icon { width: 8px; height: 8px; fill: var(--brand-blue); }
  .recipient {
    position: absolute; left: 52px; top: 168px;
    font-size: 11px; line-height: 1.35;
  }
  .recipient p + p { margin-top: 12px; }
  .letter-body {
    position: absolute; left: 52px; top: 318px; width: 470px;
    font-size: 10.5px; line-height: 1.4; color: var(--ink);
  }
  .salutation { font-weight: 700; font-size: 13px; margin-bottom: 12px; }
  .letter-body p + p { margin-top: 12px; }
  .closing { margin-top: 34px; font-size: 10.5px; }
  .signature {
    font-family: "Dancing Script", cursive;
    font-size: 36px; color: #222; margin: 4px 0 0 30px;
  }
  .footer-swoosh {
    position: absolute; left: 0; bottom: 0;
    width: 600px; height: 300px;
  }
</style>
</head>
<body>
  <main class="letterhead">
    <header>
      <div class="brand">
        <span class="brand-square"></span>
        <span class="brand-name">Northvale Clinic</span>
      </div>
      <address class="contact">
        <div>P.O Box 4410-00100</div>
        <div>Riverside, Park Lane</div>
        <div class="contact-line"><svg class="contact-icon" viewBox="0 0 10 10"><path d="M2 0h2l1 3-1.5 1a6 6 0 0 0 2.5 2.5L7 5l3 1v2c0 1-1 2-2 2C4 10 0 6 0 2c0-1 1-2 2-2z"/></svg>+254-700-4418</div>
        <div class="contact-line"><svg class="contact-icon" viewBox="0 0 10 10"><path d="M0 2h10v6H0z M0 2l5 3 5-3" /></svg>hello@northvaleclinic.com</div>
        <div class="contact-line"><svg class="contact-icon" viewBox="0 0 10 10"><circle cx="5" cy="5" r="5"/></svg>www.northvaleclinic.com</div>
      </address>
    </header>

    <section class="recipient">
      <p>Feb-03-2022</p>
      <p>Mr. Daniel Reed<br>President</p>
      <p>Harbor Legal Group<br>48 Alder Road, Suite# 12<br>Westfield, State, 240118</p>
    </section>

    <section class="letter-body">
      <p class="salutation">Dear Mr. Reed</p>
      <p>Lorem ipsum dolor sit amet, consectetur adipisicing elit, sed do eiusmod tempor incididunt ut labore et dolore magna aliqua. Ut enim ad minim veniam, quis nostrud exercitation ullamco laboris nisi ut aliquip ex ea commodo consequat. Duis aute irure dolor in reprehenderit in voluptate velit esse cillum dolore eu fugiat nulla pariatur.</p>
      <p>Lorem ipsum dolor sit amet, consectetur adipisicing elit, sed do eiusmod tempor incididunt ut labore et dolore magna aliqua. Ut enim ad minim veniam, quis nostrud exercitation ullamco laboris nisi ut aliquip ex ea commodo consequat. Duis aute irure dolor in reprehenderit in voluptate velit esse cillum dolore eu fugiat nulla pariatur.</p>
      <p>Lorem ipsum dolor sit amet, consectetur adipisicing elit, sed do eiusmod tempor incididunt ut labore et dolore magna aliqua. Ut enim ad minim veniam, quis nostrud exercitation ullamco laboris nisi ut aliquip ex ea commodo consequat.</p>
      <p>Excepteur sint occaecat cupidatat non proident, sunt in culpa qui officia deserunt mollit anim id est laborum. re et dolore magnam aliquam quaerat voluptatem.</p>
      <p class="closing">Regards</p>
      <p class="signature">Ellen Marsh</p>
    </section>

    <svg class="footer-swoosh" viewBox="0 0 600 300" preserveAspectRatio="none" aria-hidden="true">
      <path d="M370 300 C 470 270, 560 200, 600 125 L600 300 Z" fill="var(--brand-blue)"/>
      <path d="M385 262 C 470 220, 545 160, 585 108" fill="none" stroke="var(--brand-blue)" stroke-width="4" stroke-linecap="round"/>
    </svg>
  </main>
</body>
</html>
```